Corporate A4 Advert for Worldwide Timber Trader/Agent

We need a new professional company ad, which will be used in worldwide magazine publications. something sophisticated.
Our website - www.qrolumber.co.uk - for info. We are timber agents and sell timber from one part of the world to another.
I will upload a selection of product photos to include - suggest using not all but a selection of some them, to showcase the product. Our buyers purchase both logs and sawn timber
We would like this ad to list our source areas and product groups.
Our company colour is British Racing Green
Updates

Target Market(s)

timber buyers

Industry/Entity Type

Timber

Colors
00AB8E
00BBA5
67D7C9
C6EFE9
E9F9F6

Requirements
Must have
• company logo

```html
<!DOCTYPE html>
<html lang="en">
<head>
<meta charset="utf-8">
<title>QRO Timber Advert</title>
<link rel="stylesheet" href="https://fonts.googleapis.com/css2?family=Anton&family=Poppins:wght@400;500;600;700&display=swap">
<style>
  :root {
    --green: #00AB8E;
    --teal: #12B394;
    --aqua: #00BBA5;
    --cyan: #17BCD4;
    --mint: #67D7C9;
    --pale: #C6EFE9;
    --mist: #E9F9F6;
    --ink: #454545;
    --dark: #1E1E1E;
    --white: #FFFFFF;
    --wood: #B77A4A;
    --bark: #8A5A36;
    --stage: #9C9C9C;
  }
  * { margin: 0; padding: 0; box-sizing: border-box; }
  html, body { width: 1200px; height: 813px; overflow: hidden; }
  body {
    background: var(--stage);
    font-family: "Poppins", sans-serif;
    display: flex;
    justify-content: center;
    align-items: center;
  }
  .advert {
    position: relative;
    width: 573px;
    height: 813px;
    background: var(--white);
    overflow: hidden;
  }
  .top-band {
    position: absolute; left: 0; top: 0; width: 100%; height: 23px;
    background: var(--green);
  }
  .hero {
    position: absolute; left: 0; top: 23px; width: 100%; height: 288px;
  }
  .hero-photo {
    position: absolute; inset: 0;
    background:
      linear-gradient(90deg, var(--teal) 0%, rgba(18,179,148,0.92) 30%, rgba(18,179,148,0.45) 58%, rgba(18,179,148,0) 80%),
      linear-gradient(180deg, #cfe3e2 0%, #9c8a6a 25%, var(--wood) 50%, var(--bark) 75%, #7d8a4a 100%);
  }
  .headline {
    position: absolute; left: 25px; top: 36px;
    font-family: "Anton", sans-serif;
    font-weight: 400;
    font-size: 50px;
    line-height: 52px;
    color: var(--white);
    letter-spacing: -0.5px;
    text-transform: uppercase;
  }
  .brand {
    position: absolute; right: 28px; top: 150px;
    font-family: "Poppins", sans-serif;
    font-weight: 700;
    font-size: 52px;
    line-height: 1;
    color: var(--white);
    letter-spacing: 1px;
  }
  .intro-band {
    position: absolute; left: 0; top: 230px; width: 100%; height: 58px;
    background: linear-gradient(90deg, var(--cyan) 0%, rgba(23,188,212,0.9) 55%, rgba(23,188,212,0) 100%);
    padding: 14px 25px 0;
  }
  .intro-band p {
    font-size: 12px; line-height: 17px; color: var(--white); font-weight: 500;
  }
  .section-title {
    position: absolute; left: 0; width: 100%;
    text-align: center;
    font-weight: 700; font-size: 21px; color: var(--ink);
    letter-spacing: 0.3px;
  }
  .supply-title { top: 320px; }
  .products {
    position: absolute; left: 25px; top: 358px;
    display: flex; gap: 13px;
  }
  .product-card {
    width: 166px; height: 223px;
    border-radius: 8px;
    overflow: hidden;
    background: var(--teal);
    position: relative;
  }
  .product-card h3 {
    height: 42px;
    line-height: 42px;
    text-align: center;
    color: var(--white);
    font-size: 14.5px; font-weight: 700;
  }
  .product-photo {
    position: absolute; left: 0; top: 42px; width: 100%; height: 130px;
  }
  .product-photo::after {
    content: ""; position: absolute; inset: 0;
    background: linear-gradient(180deg, rgba(18,179,148,0) 45%, var(--teal) 100%);
  }
  .photo-logs { background: linear-gradient(180deg, #c9d9e4 0%, #8a7a5c 35%, var(--wood) 60%, #c49a6c 100%); }
  .photo-sawn { background: linear-gradient(180deg, #b8c3c6 0%, #6c6a66 35%, #c4715a 65%, #d98a6e 100%); }
  .photo-products { background: linear-gradient(180deg, #7fa9d6 0%, #aac9e0 45%, #5d8a64 70%, #7ea36c 100%); }
  .product-card p {
    position: absolute; left: 6px; right: 6px; bottom: 10px;
    text-align: center;
    color: var(--white);
    font-size: 11.5px; line-height: 14.5px;
  }
  .source {
    position: absolute; left: 0; top: 590px; width: 100%; height: 127px;
  }
  .source-photo {
    position: absolute; inset: 0;
    background:
      linear-gradient(180deg, var(--white) 0%, rgba(255,255,255,0.75) 35%, rgba(255,255,255,0.55) 100%),
      linear-gradient(180deg, #e2e2dc 0%, #c8a98a 55%, #b58a6a 100%);
  }
  .source-title { top: 22px; }
  .source-list {
    position: absolute; top: 55px; list-style: none;
  }
  .source-list li {
    position: relative; padding-left: 14px;
    font-size: 16px; line-height: 25px; color: var(--dark); font-weight: 500;
  }
  .source-list li::before {
    content: ""; position: absolute; left: 0; top: 10px;
    width: 6px; height: 6px; border-radius: 50%; background: var(--green);
  }
  .col-1 { left: 34px; }
  .col-2 { left: 219px; }
  .col-3 { left: 403px; }
  .divider {
    position: absolute; left: 0; top: 716px; width: 100%; height: 3px;
    background: var(--dark);
  }
  .contact {
    position: absolute; left: 0; top: 719px; width: 100%; height: 94px;
    background: linear-gradient(180deg, var(--teal) 0%, #2fbf9f 60%, #63cdb3 100%);
  }
  .contact-heading {
    position: absolute; left: 0; top: 15px; width: 170px; height: 28px;
    background: linear-gradient(90deg, var(--cyan) 0%, var(--cyan) 70%, rgba(23,188,212,0) 100%);
    padding-left: 25px;
    font-size: 21px; line-height: 28px; font-weight: 600; color: var(--white);
  }
  .contact-line {
    position: absolute; display: flex; align-items: center; gap: 6px;
    color: var(--white);
  }
  .contact-line svg { width: 13px; height: 13px; flex: none; }
  .phone { left: 25px; top: 48px; font-size: 19px; font-weight: 700; }
  .email { right: 22px; top: 22px; font-size: 17px; }
  .web { right: 39px; top: 50px; font-size: 17px; }
</style>
</head>
<body>
  <main class="advert">
    <div class="top-band"></div>

    <header class="hero">
      <div class="hero-photo" role="img" aria-label="Photo of large stacked hardwood logs in a forest yard"></div>
      <h1 class="headline">Worldwide<br>Timber Traders<br>&amp; Agents</h1>
      <div class="brand">QRO</div>
      <div class="intro-band">
        <p>We source &amp; supply quality timber and logs from<br>forest owners and sawmills worldwide.</p>
      </div>
    </header>

    <h2 class="section-title supply-title">WE SUPPLY</h2>
    <section class="products">
      <article class="product-card">
        <h3>Logs</h3>
        <div class="product-photo photo-logs" role="img" aria-label="Photo of a large felled log on a stack"></div>
        <p>High-quality logs<br>sourced worldwide</p>
      </article>
      <article class="product-card">
        <h3>Sawn Trimber</h3>
        <div class="product-photo photo-sawn" role="img" aria-label="Photo of a worker marking stacked sawn timber at a mill"></div>
        <p>A wide range of<br>sawn timber products</p>
      </article>
      <article class="product-card">
        <h3>Wood Products</h3>
        <div class="product-photo photo-products" role="img" aria-label="Photo of a timber yard with rows of logs under a blue sky"></div>
        <p>Speciality wood products,<br>such as decking, pallets,<br>profiles, and more</p>
      </article>
    </section>

    <section class="source">
      <div class="source-photo" role="img" aria-label="Faded photo of logs piled in a timber yard"></div>
      <h2 class="section-title source-title">SOURCE AREAS</h2>
      <ul class="source-list col-1"><li>North America</li><li>Europe</li></ul>
      <ul class="source-list col-2"><li>South America</li><li>Southeast Asia</li></ul>
      <ul class="source-list col-3"><li>Africa</li></ul>
    </section>

    <div class="divider"></div>

    <footer class="contact">
      <div class="contact-heading">Contact us</div>
      <div class="contact-line phone">
        <svg viewBox="0 0 16 16" aria-hidden="true"><circle cx="8" cy="8" r="8" fill="#fff"/><path d="M5.2 4.2l1.4-.2.8 2-1 .8a5.5 5.5 0 0 0 2.8 2.8l.8-1 2 .8-.2 1.4c-.1.5-.6.8-1.1.7A7.5 7.5 0 0 1 4.5 5.3c-.1-.5.2-1 .7-1.1z" fill="#12B394"/></svg>
        <span>+44 (0) 1632 960418</span>
      </div>
      <div class="contact-line email">
        <svg viewBox="0 0 16 16" aria-hidden="true"><circle cx="8" cy="8" r="8" fill="#fff"/><rect x="4" y="5" width="8" height="6" rx="1" fill="none" stroke="#12B394" stroke-width="1.2"/><path d="M4.3 5.5L8 8.5l3.7-3" fill="none" stroke="#12B394" stroke-width="1.2"/></svg>
        <span>sales@qrolumber.co.uk</span>
      </div>
      <div class="contact-line web">
        <svg viewBox="0 0 16 16" aria-hidden="true"><circle cx="8" cy="8" r="8" fill="#fff"/><g fill="none" stroke="#12B394" stroke-width="1"><circle cx="8" cy="8" r="4.5"/><ellipse cx="8" cy="8" rx="2" ry="4.5"/><path d="M3.5 8h9"/></g></svg>
        <span>www.qrolumber.co.uk</span>
      </div>
    </footer>
  </main>
</body>
</html>
```